Website for a dog poop removal service.

The Pebble Crew specializes in professional and hassle-free pet waste removal services, ensuring your yard stays clean, fresh, and safe for your family and pets. We take care of the dirty work, so you don’t have to, offering reliable, scheduled cleanups tailored to your needs. Let us help you reclaim your time and enjoy a spotless, stress-free outdoor space!
We will need the winning website to be transferred to our domain located at Servalyne. We would like to have the following web pages.
Home
About
Services
Contact Us
Client Portal
FAQ
Blog
Free Quote
The Free Quote webpage and client portal will need to be integrated with the following our account on the following website: tidyroutex.com

```html
<!DOCTYPE html>
<html lang="en">
<head>
<meta charset="utf-8">
<title>The Pebble Crew – Pet Waste Removal</title>
<link href="https://fonts.googleapis.com/css2?family=Poppins:wght@400;500;600;700&display=swap" rel="stylesheet">
<style>
:root{
  --green:#6cae3e;
  --green-light:#dcefc9;
  --green-pale:#f3f8ec;
  --orange:#f7931e;
  --tan:#b8956a;
  --beige:#e8dccb;
  --card-beige:#e6d8c9;
  --pink:#fde7ea;
  --navy:#1f3a78;
  --ink:#2f2f2f;
  --text:#444;
  --footer:#2a2929;
  --white:#fff;
}
*{box-sizing:border-box;margin:0;padding:0}
html,body{width:1200px;height:4216px;overflow:hidden}
body{font-family:'Poppins',sans-serif;color:var(--text);background:var(--white);position:relative}
.abs{position:absolute}
section,header,footer{position:absolute;left:0;width:1200px}
.pill{position:absolute;display:flex;align-items:center;justify-content:center;gap:8px;border-radius:30px;color:#fff;font-size:13px;font-weight:500;white-space:nowrap}
.pill.green{background:var(--green)}
.pill.orange{background:var(--orange)}
.heading{position:absolute;left:0;width:1200px;text-align:center;font-size:36px;font-weight:400;color:var(--tan)}
.heading b{font-weight:600;color:var(--green)}
.underline{position:absolute;height:2px;background:var(--ink)}
/* header */
.site-header{top:0;height:103px;background:#fff}
.brand{position:absolute;left:140px;top:22px;display:flex;align-items:center;gap:10px}
.brand-mark{width:52px;height:52px;border-radius:50%;background:var(--green)}
.brand-name{font-size:20px;font-weight:700;color:var(--ink);line-height:1.05;width:130px}
.topbar{position:absolute;top:8px;right:142px;display:flex;align-items:center;gap:8px;font-size:12px;color:#555}
.social-dot{width:20px;height:20px;border-radius:50%;border:1.5px solid var(--green)}
.phone-dot{width:20px;height:20px;border-radius:50%;border:1.5px solid var(--green);display:flex;align-items:center;justify-content:center;margin-left:26px}
.nav{position:absolute;top:61px;right:270px;display:flex;gap:28px;font-size:12px;font-weight:500;color:var(--navy);white-space:nowrap}
/* hero */
.hero{top:103px;height:522px;background:var(--beige);overflow:hidden}
.hero-visual{position:absolute;left:0;top:0}
.hero h1{position:absolute;left:142px;top:90px;font-size:34px;line-height:39px;font-weight:700;color:#333}
.hero h1 span{color:var(--green)}
.hero .lead{position:absolute;left:142px;top:183px;width:300px;font-size:14px;line-height:22px;color:#222}
.hero h3{position:absolute;left:142px;top:306px;font-size:17px;font-weight:600;color:#222}
.benefits{position:absolute;left:142px;top:337px;list-style:none;font-size:14px;color:#222}
.benefits li{display:flex;align-items:center;gap:7px;height:22px}
.chev{width:13px;height:13px;border:1px solid #555;border-radius:50%}
.mascot{position:absolute;border-radius:50% 50% 45% 45%;background:linear-gradient(180deg,#f4efe6 0%,#e9e2d5 55%,#9fd06f 80%,#6cae3e 100%)}
/* about */
.about{top:625px;height:653px;background:#fff}
.about h2{position:absolute;left:635px;top:192px;font-size:36px;font-weight:400;color:var(--tan)}
.about h2 b{color:var(--green);font-weight:600}
.about p{position:absolute;left:635px;width:425px;font-size:14px;line-height:21px;color:#333}
/* why */
.why{top:1278px;height:580px;background:var(--pink)}
.feature{position:absolute;width:230px}
.feature h4{font-size:15.5px;font-weight:500;color:var(--navy);margin-bottom:4px}
.feature p{font-size:13px;line-height:21px;color:#444}
.feature.left{text-align:right}
.ficon{position:absolute;width:76px;height:76px;border-radius:50%;background:#f5f9ea;border:5px solid #e3f0cc;display:flex;align-items:center;justify-content:center}
/* services */
.services{top:1858px;height:657px;background:#fff}
.services h3{position:absolute;left:0;width:1200px;text-align:center;top:145px;font-size:21px;font-weight:600;color:var(--navy)}
.card{position:absolute;top:204px;width:212px;height:266px;border-radius:16px;text-align:center;padding:0 12px}
.card.outline{border:1.5px solid #ddd;background:#fff}
.card.beige{background:var(--card-beige)}
.card.mint{background:var(--green-light)}
.card .icon{width:64px;height:64px;margin:16px auto 0;border-radius:50%;background:#f0ece6}
.card h4{margin-top:24px;font-size:15.5px;font-weight:600;color:#222}
.card p{margin-top:12px;font-size:12.5px;line-height:19px;color:#444}
.card .go{position:absolute;left:86px;bottom:-20px;width:40px;height:40px;border-radius:50%;background:var(--green);display:flex;align-items:center;justify-content:center}
/* faq */
.faq{top:2515px;height:640px;background:var(--green-pale)}
.q{position:absolute;left:247px;width:706px;height:48px;border:1.5px solid #ddd;background:#fff;border-radius:4px;display:flex;align-items:center;justify-content:space-between;padding:0 22px;font-size:15px;color:#222}
.q.open{border-color:var(--green);color:var(--green)}
.answer{position:absolute;left:271px;width:640px;top:226px;font-size:12.5px;line-height:23px;color:#444}
/* contact */
.contact{top:3155px;height:620px;background:#fff}
.field{position:absolute;background:#fff;box-shadow:0 2px 12px rgba(0,0,0,.09);border-radius:4px;display:flex;align-items:center;justify-content:space-between;padding:0 18px;font-size:13px;color:#333}
.field.area{align-items:flex-start;padding-top:16px}
.ficon2{width:16px;height:14px;background:var(--tan);border-radius:2px}
/* footer */
.site-footer{top:3775px;height:441px;background:var(--footer);color:#ddd}
.site-footer h5{position:absolute;top:92px;font-size:16px;font-weight:500;color:var(--green)}
.site-footer .bar{position:absolute;top:120px;width:34px;height:2px;background:var(--green)}
.flinks{position:absolute;top:135px;list-style:none;font-size:12.5px}
.flinks li{display:flex;align-items:center;gap:8px;height:25.5px}
.ring{width:10px;height:10px;border-radius:50%;border:1px solid var(--green)}
.fsocial{position:absolute;top:135px;list-style:none;font-size:12.5px}
.fsocial li{display:flex;align-items:center;gap:10px;height:39px}
.fsocial .c{width:24px;height:24px;border-radius:50%;border:1.5px solid var(--green)}
.fcontact{position:absolute;left:833px;top:137px;font-size:12.5px;line-height:15px}
.fcontact .row{display:flex;gap:12px;margin-bottom:22px}
.fcontact b{display:block;font-weight:500;color:#fff}
.copyright{position:absolute;bottom:14px;left:0;width:1200px;text-align:center;font-size:12.5px;color:#ddd}
</style>
</head>
<body>

<header class="site-header">
  <div class="brand"><div class="brand-mark"></div><div class="brand-name">The Pebble Crew</div></div>
  <div class="topbar">
    <span>Follow on:</span>
    <span class="social-dot"></span><span class="social-dot"></span><span class="social-dot"></span><span class="social-dot"></span>
    <span class="phone-dot"><svg width="10" height="10" viewBox="0 0 24 24"><path d="M6 2l4 4-2 3a12 12 0 007 7l3-2 4 4-3 4C10 21 3 14 2 5z" fill="#333"/></svg></span>
    <span>(123) 456-7890</span>
  </div>
  <nav class="nav"><span>Home</span><span>About</span><span>Services</span><span>Faqs</span><span>Blog</span><span>Contact Us</span></nav>
  <div class="pill green" style="left:953px;top:48px;width:106px;height:42px;font-weight:600">Free Quote</div>
</header>

<section class="hero">
  <svg class="hero-visual" width="1200" height="580" viewBox="0 0 1200 580">
    <defs>
      <linearGradient id="photoTone" x1="0" y1="0" x2="1" y2="1">
        <stop offset="0" stop-color="#6f8f4c"/><stop offset=".5" stop-color="#8a7057"/><stop offset="1" stop-color="#a79a88"/>
      </linearGradient>
    </defs>
    <path d="M1200 0 L780 0 C700 60 610 120 615 240 C620 390 700 580 800 578 C900 576 1000 500 1200 420 Z" fill="var(--orange)"/>
    <path role="img" aria-label="Photo of a smiling couple crouching with their brown dog on a backyard path" d="M1200 0 L800 0 C720 70 640 140 645 250 C650 380 720 555 810 555 C900 555 1000 480 1200 405 Z" fill="url(#photoTone)"/>
  </svg>
  <h1>KEEPING YOUR YARD <span>CLEAN,</span><br><span>FRESH, AND HASSLE-FREE!</span></h1>
  <p class="lead">Professional pet waste removal services tailored to your needs.</p>
  <div class="pill green" style="left:142px;top:247px;width:190px;height:40px;font-weight:600">Get a Free Quote Today</div>
  <h3>Key Benefits</h3>
  <ul class="benefits">
    <li><span class="chev"></span>Reliable, Scheduled Cleanups</li>
    <li><span class="chev"></span>Safe for Pets and Family</li>
    <li><span class="chev"></span>Affordable and Hassle-Free</li>
    <li><span class="chev"></span>Environmentally Responsible Disposal</li>
  </ul>
  <div class="mascot" role="img" aria-label="Cartoon dog mascot holding a scooper on a patch of grass" style="left:478px;top:327px;width:178px;height:210px"></div>
</section>

<section class="about">
  <svg class="abs" style="left:130px;top:100px" width="460" height="500" viewBox="0 0 460 500">
    <defs><linearGradient id="aboutTone" x1="0" y1="0" x2="1" y2="1"><stop offset="0" stop-color="#6f6a3e"/><stop offset=".6" stop-color="#8d8a6a"/><stop offset="1" stop-color="#b7b4a0"/></linearGradient></defs>
    <path role="img" aria-label="Photo of a dachshund next to a green scooper collecting waste on the lawn" d="M60 40 C150 -10 260 40 330 110 C420 200 460 280 400 340 C330 410 250 470 170 470 C80 470 10 400 12 300 C14 200 -20 90 60 40 Z" fill="url(#aboutTone)"/>
  </svg>
  <h2>About <b>Pebble Crew</b></h2>
  <p style="top:254px">We're passionate about making life easier for pet owners. Our professional team is dedicated to ensuring your yard stays clean, healthy, and stress-free. With flexible scheduling, affordable rates, and top-notch customer service, we make pet ownership even more enjoyable.</p>
  <p style="top:373px">The Pebble Crew specializes in professional and hassle-free pet waste removal services, ensuring your yard stays clean, fresh, and safe for your family and pets.</p>
  <div class="pill green" style="left:635px;top:456px;width:132px;height:40px">Read More <svg width="16" height="12" viewBox="0 0 16 12"><path d="M0 6h14M9 1l5 5-5 5" stroke="#fff" stroke-width="2" fill="none"/></svg></div>
</section>

<section class="why">
  <div class="heading" style="top:78px">Why <b>Choose</b> Us?</div>
  <div class="underline" style="left:543px;top:130px;width:98px"></div>
  <svg class="abs" style="left:400px;top:117px" width="400" height="420" viewBox="0 0 400 420">
    <circle cx="200" cy="188" r="188" fill="none" stroke="var(--orange)" stroke-width="1.3" stroke-dasharray="5 4"/>
  </svg>
  <div class="mascot" role="img" aria-label="Cartoon dog mascot with a green bandana and a scooper" style="left:490px;top:177px;width:215px;height:250px"></div>
  <div class="ficon" style="left:405px;top:167px"><svg width="30" height="30" viewBox="0 0 24 24"><path d="M12 2l8 3v6c0 5-4 9-8 11-4-2-8-6-8-11V5z M8 12l3 3 5-6" fill="none" stroke="#333" stroke-width="1.5"/></svg></div>
  <div class="ficon" style="left:718px;top:167px"><svg width="30" height="30" viewBox="0 0 24 24"><path d="M4 20C4 10 10 4 20 4c0 10-6 16-16 16zM4 20l10-10" fill="none" stroke="#333" stroke-width="1.5"/></svg></div>
  <div class="ficon" style="left:405px;top:356px"><svg width="30" height="30" viewBox="0 0 24 24"><circle cx="12" cy="12" r="9" fill="none" stroke="#333" stroke-width="1.5"/><path d="M8 12l3 3 5-6" fill="none" stroke="#333" stroke-width="1.5"/></svg></div>
  <div class="ficon" style="left:718px;top:356px"><svg width="30" height="30" viewBox="0 0 24 24"><path d="M3 11l9-7 9 7v10H3z M9 21v-6h6v6" fill="none" stroke="#333" stroke-width="1.5"/></svg></div>
  <div class="feature left" style="left:160px;top:182px"><h4>Reliable Service</h4><p>Always on time, always thorough</p></div>
  <div class="feature" style="left:807px;top:182px"><h4>Pet &amp; Eco-Friendly</h4><p>Safe disposal methods and eco-conscious practices</p></div>
  <div class="feature left" style="left:160px;top:378px"><h4>Satisfaction Guaranteed</h4><p>We're not happy unless you're happy!</p></div>
  <div class="feature" style="left:807px;top:378px"><h4>Locally Owned &amp; Operated</h4><p>Supporting our community, one yard at a time</p></div>
</section>

<section class="services">
  <div class="heading" style="top:76px">Our <b>Services</b></div>
  <div class="underline" style="left:560px;top:126px;width:80px"></div>
  <h3>Our Services Tailored to Your Needs</h3>
  <div class="card outline" style="left:142px"><div class="icon"></div><h4>Weekly Cleanups</h4><p>Keep your yard spotless with our regular cleanup services. Ideal for maintaining a fresh and clean outdoor space.</p><span class="go"><svg width="14" height="14" viewBox="0 0 14 14"><path d="M2 12L12 2M5 2h7v7" stroke="#fff" stroke-width="1.6" fill="none"/></svg></span></div>
  <div class="card beige" style="left:377px"><div class="icon" style="background:transparent"></div><h4>One-Time Cleanups</h4><p>Need help before a special event or after a busy week? We've got you covered with our one-time cleanup service.</p><span class="go"><svg width="14" height="14" viewBox="0 0 14 14"><path d="M2 12L12 2M5 2h7v7" stroke="#fff" stroke-width="1.6" fill="none"/></svg></span></div>
  <div class="card outline" style="left:611px"><div class="icon"></div><h4>Custom Schedules</h4><p>Choose a schedule that fits your lifestyle. We offer flexible options to ensure your yard stays pristine.</p><span class="go"><svg width="14" height="14" viewBox="0 0 14 14"><path d="M2 12L12 2M5 2h7v7" stroke="#fff" stroke-width="1.6" fill="none"/></svg></span></div>
  <div class="card mint" style="left:846px"><div class="icon" style="background:#cbe4b4"></div><h4>Commercial Services</h4><p>Perfect for parks, apartment complexes, and other dog-friendly spaces. Let us handle the mess while you focus on your property.</p><span class="go"><svg width="14" height="14" viewBox="0 0 14 14"><path d="M2 12L12 2M5 2h7v7" stroke="#fff" stroke-width="1.6" fill="none"/></svg></span></div>
  <div class="pill orange" style="left:529px;top:530px;width:141px;height:41px">View Details <svg width="16" height="12" viewBox="0 0 16 12"><path d="M0 6h14M9 1l5 5-5 5" stroke="#fff" stroke-width="2" fill="none"/></svg></div>
</section>

<section class="faq">
  <div class="heading" style="top:77px">Frequently <b>Asked Questions</b></div>
  <div class="underline" style="left:553px;top:128px;width:96px"></div>
  <div class="q open" style="top:165px"><span>What does your dog poop removal service include?</span><svg width="14" height="14" viewBox="0 0 14 14"><path d="M7 13V1M2 6l5-5 5 5" stroke="var(--green)" stroke-width="1.5" fill="none"/></svg></div>
  <p class="answer">Need help before a special event or after a busy week? We've got you covered with our one-time cleanup service.</p>
  <div class="q" style="top:300px"><span>Do you service all yard sizes?</span><svg width="14" height="12" viewBox="0 0 14 12"><path d="M0 6h13M8 1l5 5-5 5" stroke="#222" stroke-width="1.5" fill="none"/></svg></div>
  <div class="q" style="top:364px"><span>How often can I schedule your services?</span><svg width="14" height="12" viewBox="0 0 14 12"><path d="M0 6h13M8 1l5 5-5 5" stroke="#222" stroke-width="1.5" fill="none"/></svg></div>
  <div class="q" style="top:428px"><span>Are you environmentally friendly?</span><svg width="14" height="12" viewBox="0 0 14 12"><path d="M0 6h13M8 1l5 5-5 5" stroke="#222" stroke-width="1.5" fill="none"/></svg></div>
  <div class="pill orange" style="left:542px;top:512px;width:116px;height:41px">View All <svg width="16" height="12" viewBox="0 0 16 12"><path d="M0 6h14M9 1l5 5-5 5" stroke="#fff" stroke-width="2" fill="none"/></svg></div>
</section>

<section class="contact">
  <div class="heading" style="top:77px">Let's Keep <b>Your Yard Clean!</b></div>
  <div class="underline" style="left:541px;top:128px;width:90px"></div>
  <div class="field" style="left:177px;top:168px;width:413px;height:55px"><span>First Name</span><span class="ficon2" style="border-radius:50% 50% 2px 2px"></span></div>
  <div class="field" style="left:615px;top:168px;width:407px;height:55px"><span>Last Name</span><span class="ficon2" style="border-radius:50% 50% 2px 2px"></span></div>
  <div class="field" style="left:177px;top:242px;width:413px;height:55px"><span>Email Address</span><span class="ficon2"></span></div>
  <div class="field" style="left:615px;top:242px;width:407px;height:55px"><span>Subject</span><span class="ficon2"></span></div>
  <div class="field area" style="left:177px;top:315px;width:845px;height:142px"><span>Type Message...</span><span class="ficon2"></span></div>
  <div class="pill orange" style="left:531px;top:497px;width:138px;height:41px">Submit Now <svg width="16" height="12" viewBox="0 0 16 12"><path d="M0 6h14M9 1l5 5-5 5" stroke="#fff" stroke-width="2" fill="none"/></svg></div>
</section>

<footer class="site-footer">
  <div class="abs" style="left:142px;top:112px;display:flex;align-items:center;gap:12px">
    <div style="width:72px;height:72px;border-radius:50%;background:var(--green)"></div>
    <div style="font-size:24px;font-weight:700;color:#fff;line-height:1.05;width:160px">The Pebble Crew</div>
  </div>
  <p class="abs" style="left:142px;top:213px;width:270px;font-size:12.5px;line-height:19px">Ready to schedule your cleanup or have questions? We'd love to hear from you.</p>

  <h5 style="left:459px">Quick Links</h5><div class="bar" style="left:466px"></div>
  <ul class="flinks" style="left:461px">
    <li><span class="ring"></span>Home</li><li><span class="ring"></span>About</li><li><span class="ring"></span>Services</li><li><span class="ring"></span>Faq's</li><li><span class="ring"></span>Blog</li><li><span class="ring"></span>Free Quote</li><li><span class="ring"></span>Contact Us</li>
  </ul>

  <h5 style="left:671px">Follow Us</h5><div class="bar" style="left:678px"></div>
  <ul class="fsocial" style="left:674px">
    <li><span class="c"></span>Pawbook</li><li><span class="c"></span>Chirper</li><li><span class="c"></span>Worklink</li><li><span class="c"></span>Snapgram</li>
  </ul>

  <h5 style="left:833px">Contact Details</h5><div class="bar" style="left:840px"></div>
  <div class="fcontact">
    <div class="row"><svg width="12" height="16" viewBox="0 0 12 16"><path d="M6 0a6 6 0 016 6c0 4-6 10-6 10S0 10 0 6a6 6 0 016-6z" fill="var(--tan)"/><circle cx="6" cy="6" r="2" fill="var(--footer)"/></svg><div><b>Address</b>4820 W Meadowlark Ln,<br>Fairview, ID 83700</div></div>
    <div class="row"><svg width="12" height="12" viewBox="0 0 24 24"><path d="M6 2l4 4-2 3a12 12 0 007 7l3-2 4 4-3 4C10 21 3 14 2 5z" fill="var(--tan)"/></svg><div><b>Phone</b>(123) 456-7890</div></div>
    <div class="row"><svg width="13" height="10" viewBox="0 0 13 10"><rect width="13" height="10" fill="var(--tan)"/><path d="M0 0l6.5 5L13 0" stroke="var(--footer)" fill="none"/></svg><div><b>Email</b>info@thepebblecrew.com</div></div>
  </div>
  <p class="copyright">Copyright © 2025 The Pebble Crew. All Rights Reserved.</p>
</footer>

</body>
</html>
```